Business Card Design

We need a basic, but modern design card. Our business is a local Queanbeyan/Canberra courier service, but can organise interstate delivery if needed. Our fleet ranges from 1 tonne vans to 8 tonne trucks.

Industry/Entity Type

Business

Contact Information for Business Card

Harbourline Freight
14 Tarrant Road
Marlow Creek NSW 2631

Owen Prescott
CEO

Phone: 02 61847315
Fax: 02 61847398
email: owen@harbourlinefreight.com.au

```html
<!DOCTYPE html>
<html lang="en">
<head>
<meta charset="utf-8">
<title>Harbourline Freight — Business Card</title>
<link href="https://fonts.googleapis.com/css2?family=Jost:ital,wght@0,300;0,400;0,700;1,700&display=swap" rel="stylesheet">
<style>
  :root {
    --navy: #0a4486;
    --navy-deep: #063a73;
    --navy-light: #0553a0;
    --red: #e31e2a;
    --grey-row: #c8c9c9;
    --grey-light: #e6e6e6;
    --ink: #333333;
    --white: #ffffff;
    --page: #ffffff;
  }
  * { box-sizing: border-box; margin: 0; padding: 0; }
  html, body {
    width: 1200px; height: 1003px; overflow: hidden;
    background: var(--page);
    font-family: "Jost", "Futura", sans-serif;
  }
  .card {
    position: absolute; left: 190px; top: 274px;
    width: 820px; height: 455px;
    display: flex;
  }
  .brand-panel {
    position: relative;
    width: 382px; height: 100%;
    background: linear-gradient(180deg, var(--navy-deep) 0%, var(--navy-light) 100%);
    color: var(--white);
  }
  .brand-name {
    position: absolute; left: 0; right: 0; top: 168px;
    text-align: center;
    font-weight: 700; font-size: 31px; line-height: 1.05;
    text-transform: uppercase; letter-spacing: 1px;
  }
  .brand-tagline {
    position: absolute; left: 0; right: 0; top: 238px;
    text-align: center;
    font-weight: 400; font-size: 14px; letter-spacing: 8px;
    padding-left: 8px;
  }
  .fleet-art {
    position: absolute; left: 128px; top: 284px;
    width: 144px; height: 114px;
    border-radius: 6px;
    background: linear-gradient(180deg, rgba(255,255,255,0.10), rgba(255,255,255,0.03));
  }
  .info-panel {
    position: relative; flex: 1; height: 100%;
    background: var(--grey-light);
  }
  .info-panel::before {
    content: ""; position: absolute; left: 0; top: 0;
    width: 34px; height: 146px;
    background: linear-gradient(90deg, rgba(0,0,0,0.45), rgba(0,0,0,0));
  }
  .person {
    height: 146px;
    display: flex; flex-direction: column; align-items: center; justify-content: center;
  }
  .person-name {
    color: var(--navy); font-weight: 700; font-style: italic;
    font-size: 40px; line-height: 1; margin-top: 8px;
  }
  .person-title {
    color: var(--red); font-weight: 400; font-size: 20px;
    letter-spacing: 9px; margin-top: 6px; padding-left: 9px;
  }
  .contact-row {
    display: flex; height: 77.25px;
  }
  .contact-row.is-shaded { background: var(--grey-row); }
  .contact-icon {
    width: 77px; flex: none;
    display: flex; align-items: center; justify-content: center;
  }
  .contact-icon.is-red { background: linear-gradient(90deg, #9c1017 0%, var(--red) 45%); }
  .contact-icon.is-navy { background: linear-gradient(90deg, #031f40 0%, var(--navy) 45%); }
  .contact-icon svg { width: 32px; height: 32px; }
  .contact-text {
    display: flex; flex-direction: column; justify-content: center;
    padding-left: 17px;
    color: var(--ink); font-weight: 300; font-size: 23px; line-height: 1.15;
    white-space: nowrap;
  }
</style>
</head>
<body>
  <div class="card">
    <section class="brand-panel">
      <div class="brand-name">Harbourline<br>Freight</div>
      <div class="brand-tagline">ON THE MOVE</div>
      <div class="fleet-art" role="img" aria-label="Faint illustration of a delivery truck"></div>
    </section>

    <section class="info-panel">
      <header class="person">
        <div class="person-name">Owen Prescott</div>
        <div class="person-title">CEO</div>
      </header>

      <div class="contact-row is-shaded">
        <div class="contact-icon is-red">
          <svg viewBox="0 0 32 32" aria-hidden="true">
            <path d="M16 2a10 10 0 0 0-10 10c0 8 10 18 10 18s10-10 10-18A10 10 0 0 0 16 2z" fill="#fff"/>
            <circle cx="16" cy="12" r="5" fill="none" stroke="#e31e2a" stroke-width="2.5"/>
          </svg>
        </div>
        <div class="contact-text">
          <span>14 Tarrant Road Marlow Creek</span>
          <span>NSW 2631</span>
        </div>
      </div>

      <div class="contact-row">
        <div class="contact-icon is-navy">
          <svg viewBox="0 0 32 32" aria-hidden="true">
            <path d="M9 3l4 6-2.5 3c1.5 4 4.5 7.5 8 9.5l3-2.5 6 4-2 4.5C18 28 6 16 5 6z" fill="#fff"/>
          </svg>
        </div>
        <div class="contact-text">
          <span>Tel&nbsp; : 02 61847315</span>
          <span>Fax : 02 61847398</span>
        </div>
      </div>

      <div class="contact-row is-shaded">
        <div class="contact-icon is-red">
          <svg viewBox="0 0 32 32" aria-hidden="true">
            <rect x="5" y="8" width="22" height="16" fill="none" stroke="#fff" stroke-width="2"/>
            <path d="M5 8l11 9 11-9" fill="none" stroke="#fff" stroke-width="2"/>
          </svg>
        </div>
        <div class="contact-text">
          <span>owen@harbourlinefreight.com.au</span>
        </div>
      </div>

      <div class="contact-row">
        <div class="contact-icon is-navy">
          <svg viewBox="0 0 32 32" aria-hidden="true">
            <g fill="none" stroke="#fff" stroke-width="2">
              <circle cx="16" cy="16" r="11"/>
              <ellipse cx="16" cy="16" rx="5" ry="11"/>
              <path d="M5 16h22M7 10h18M7 22h18"/>
            </g>
          </svg>
        </div>
        <div class="contact-text">
          <span>www.harbourlinefreight.com.au</span>
        </div>
      </div>
    </section>
  </div>
</body>
</html>
```